Website for company called VELQUOgen

We need a website for our new company called VELQUOgen which developed a platform/technology to identify antigen-specific T cells (immune cells) which can be used for cancer therapy, autoimmunity, etc.

The platform is called VELQUO and is rapid, versatile, unbiased, and inexpensive.

We have a semi-final logo although we are not completely set on color and font of text (attached).

Target Market(s)

Our target audience at the moment would be potential investors and VCs. We eventually are interested in getting attention from scientists and cell/immunotherapy companies.

Industry/Entity Type

Healthcare/Technology

Coding

Coded - Design and coding required

Number of Pages Required

1 page

Colors
0094D4
00A9DD
6FCCEA
C7EBF8
E9F6FB
00AB8E
00BBA5
67D7C9
C6EFE9
E9F9F6
E54698
E96AAD
F1A4CE
F9D9EA
FCEFF6
A7469A
B969AE
D3A5CF
EDDBEB
F8F0F9
6B429C
8869AF
B7A5CE
E3DAEB
F3F0F8

Requirements
Must have
• Landing page about the company, About us page, Technology page (could be merged with company landing page), Contact us page

```html
<!DOCTYPE html>
<html lang="en">
<head>
<meta charset="utf-8">
<title>VELQUOgen — Revolutionizing T-Cell Discovery</title>
<link href="https://fonts.googleapis.com/css2?family=Poppins:wght@400;500;600;700&family=Montserrat:wght@400;500;600&display=swap" rel="stylesheet">
<style>
:root{
  --blue:#0094D4;
  --blue-2:#00A9DD;
  --blue-soft:#C7EBF8;
  --blue-pale:#E9F6FB;
  --green:#00AB8E;
  --green-2:#00BBA5;
  --navy:#16262f;
  --ink:#1f2a33;
  --text:#4a5560;
  --line:#dfe6ea;
  --white:#ffffff;
  --star:#f7a21b;
}
*{box-sizing:border-box;margin:0;padding:0}
html,body{width:1200px;height:4528px;overflow:hidden;background:var(--white)}
body{font-family:"Montserrat",sans-serif;color:var(--text);position:relative}
.page{position:relative;width:1200px;height:4528px;overflow:hidden}
.abs{position:absolute}
h1,h2,h3,.heading{font-family:"Poppins",sans-serif;color:var(--ink)}
.eyebrow{font-family:"Poppins",sans-serif;font-size:16px;font-weight:500;letter-spacing:2.5px;color:var(--blue);text-transform:uppercase}
.section-title{font-size:31px;font-weight:500;color:var(--ink);line-height:1.2}
.divider{display:flex;gap:6px}
.divider span{display:block;width:18px;height:2px;background:var(--blue)}
.divider span:nth-child(2){background:var(--ink)}
.center{left:0;width:1200px;text-align:center}
.center .divider,.divider.centered{justify-content:center}
.btn{position:absolute;display:flex;align-items:center;justify-content:center;font-family:"Poppins",sans-serif;font-size:14px;font-weight:500;border-radius:2px}
.btn-solid{background:var(--blue);color:var(--white)}
.btn-outline{border:1.5px solid rgba(255,255,255,.85);color:var(--white)}
.photo{position:absolute;overflow:hidden}

/* header */
.topbar{top:0;left:0;width:1200px;height:70px;background:var(--white)}
.brand{display:flex;align-items:center;gap:8px;font-family:"Poppins",sans-serif;font-weight:600;font-size:26px;color:var(--ink)}
.brand i{display:block;width:22px;height:22px;border-radius:50%;background:var(--blue)}
.call{left:782px;top:18px;display:flex;align-items:center;gap:10px}
.call-icon{width:24px;height:24px;border-radius:50%;background:var(--blue-soft);display:flex;align-items:center;justify-content:center}
.call small{display:block;font-size:10px;color:var(--text)}
.call b{display:block;font-size:14px;font-weight:600;color:var(--ink)}
.nav{top:70px;left:0;width:1200px;height:43px;background:var(--blue)}
.nav a{position:absolute;top:13px;font-family:"Poppins",sans-serif;font-size:14px;color:var(--white);text-decoration:none}

/* hero */
.hero{top:113px;left:0;width:1200px;height:600px;background:linear-gradient(100deg,#0c2433 0%,#173b52 40%,#8fa7b6 75%,#d9e1e6 100%)}
.hero-label{left:144px;top:187px;display:flex;align-items:center;gap:10px;font-size:14px;font-weight:500;color:var(--blue-2);letter-spacing:.5px}
.hero-label::before{content:"";width:34px;height:1.5px;background:var(--blue-2)}
.hero-title{left:144px;top:218px;color:var(--white);font-family:"Poppins",sans-serif;font-weight:700;line-height:1.2}
.hero-title .l1{font-size:42px;display:block}
.hero-title .l2{font-size:52px;display:block}
.hero-text{left:144px;top:357px;width:480px;font-size:13.5px;line-height:26px;color:#e3ecf2}
.scroll-cue{left:576px;top:650px;width:48px;height:48px;border-radius:50%;background:var(--white);box-shadow:0 4px 14px rgba(0,0,0,.15);display:flex;align-items:center;justify-content:center}

/* platform */
.feature{position:absolute;top:861px;width:211px;height:218px;border:1px solid var(--line);background:var(--white);padding:22px 16px 0}
.feature.active{background:var(--blue-pale);border-color:var(--blue-pale)}
.feature h3{margin-top:22px;font-size:17px;font-weight:500;color:var(--ink)}
.feature p{margin-top:9px;font-size:12.5px;line-height:22px;color:var(--text)}

/* about */
.about-text{left:599px;width:470px}
.body-copy{font-size:12.5px;line-height:20.5px;color:var(--text)}
.link{position:absolute;font-family:"Poppins",sans-serif;font-size:14px;font-weight:500;color:var(--blue)}

/* stats */
.stats{top:1646px;left:0;width:1200px;height:257px;background:linear-gradient(90deg,var(--green) 0%,#18c0a6 50%,var(--green) 100%)}
.stat{position:absolute;top:80px;width:240px;text-align:center;color:var(--white)}
.stat b{display:block;font-family:"Poppins",sans-serif;font-size:42px;font-weight:500;line-height:1.1}
.stat span{display:block;margin-top:12px;font-size:16px}
.stat-sep{position:absolute;top:76px;width:1px;height:110px;background:rgba(255,255,255,.35)}

/* team */
.check{position:absolute;display:flex;align-items:center;gap:8px;font-size:12.5px;font-weight:500;color:var(--ink)}
.check i{width:18px;height:18px;border-radius:50%;background:var(--green);display:flex;align-items:center;justify-content:center}

/* applications */
.app{position:absolute;top:2550px;height:309px;background:var(--white);box-shadow:0 2px 10px rgba(0,0,0,.06);text-align:center}
.app .photo{left:0;top:0;width:100%;height:177px}
.app h3{margin-top:194px;font-size:17px;font-weight:500;color:var(--ink)}
.app p{margin:10px auto 0;width:240px;font-size:12.5px;line-height:21px;color:var(--text)}

/* investment */
.invest{top:3011px;left:0;width:1200px;height:577px;background:linear-gradient(180deg,#1a8fd1 0%,var(--blue) 60%,#0b8bd0 100%)}
.invest .eyebrow{color:var(--white)}
.invest .section-title{color:var(--white)}
.invest .divider span{background:var(--white)}
.invest .divider span:nth-child(2){background:var(--blue-soft)}
.ibox{position:absolute;top:3192px;width:289px;height:225px;background:var(--white);text-align:center;padding-top:32px}
.ibox .ico{margin:0 auto;width:64px;height:64px;border-radius:50%;background:var(--blue-pale);display:flex;align-items:center;justify-content:center}
.ibox .ico.strong{background:var(--blue)}
.ibox h3{margin-top:16px;font-size:14.5px;font-weight:600;color:var(--ink)}
.ibox p{margin:8px auto 0;width:230px;font-size:11.5px;line-height:20px;color:var(--text)}
.btn-line{border:1.5px solid rgba(255,255,255,.7);background:rgba(255,255,255,.08);color:var(--white);font-size:13.5px}

/* testimonial */
.quote-card{left:404px;top:3821px;width:648px;height:217px;border:1.5px solid var(--blue-soft);border-radius:14px;background:var(--white);padding:30px 40px 0 40px}
.stars{display:flex;gap:4px}
.quote-card p{margin-top:14px;font-size:13px;line-height:24px;color:var(--ink)}
.person{display:flex;align-items:center;gap:12px;margin-top:16px}
.avatar{width:40px;height:40px;border-radius:50%;background:linear-gradient(135deg,#b89a86,#6f5446)}
.person b{display:block;font-size:13px;font-weight:600;color:var(--ink)}
.person span{display:block;font-size:12px;color:var(--text);margin-top:3px}
.arrow-btn{position:absolute;left:1034px;width:26px;height:26px;border-radius:50%;background:var(--white);border:1px solid var(--line);display:flex;align-items:center;justify-content:center}

/* footer */
.footer{top:4155px;left:0;width:1200px;height:373px;background:var(--navy);color:#c9d2d8}
.footer .brand{color:var(--white)}
.footer h4{position:absolute;top:85px;font-family:"Poppins",sans-serif;font-size:15px;font-weight:500;color:var(--white)}
.flist{position:absolute;top:122px;list-style:none}
.flist li{display:flex;align-items:center;gap:10px;height:29px;font-size:13px;color:#c9d2d8}
.flist li::before{content:"+";color:var(--blue-2);font-size:16px;font-weight:600}
.fcontact{position:absolute;left:822px;display:flex;align-items:center;gap:14px;font-size:13px;line-height:21px;color:#c9d2d8}
.fcontact i{width:30px;height:30px;border-radius:50%;background:#24363f;display:flex;align-items:center;justify-content:center;flex:none}
.fcontact i.blue{background:var(--blue)}
.social{width:20px;height:20px;border-radius:50%;border:1px solid #8d9aa2;display:inline-block}
.social.on{background:var(--blue);border-color:var(--blue)}
.legal{top:305px;left:144px;width:912px;border-top:1px solid #2d3e47;padding-top:18px;display:flex;justify-content:space-between;font-size:11px;color:#9aa7ae}
.legal u{color:var(--white)}
</style>
</head>
<body>
<div class="page">

<!-- Header -->
<header class="abs topbar">
  <div class="abs brand" style="left:144px;top:17px"><i></i>VELQUOgen</div>
  <div class="abs call">
    <div class="call-icon"><svg width="12" height="12" viewBox="0 0 24 24"><path d="M6.6 10.8a15 15 0 0 0 6.6 6.6l2.2-2.2a1 1 0 0 1 1-.25 11.4 11.4 0 0 0 3.6.57 1 1 0 0 1 1 1V20a1 1 0 0 1-1 1A17 17 0 0 1 3 4a1 1 0 0 1 1-1h3.5a1 1 0 0 1 1 1c0 1.25.2 2.45.57 3.57a1 1 0 0 1-.25 1z" fill="#0094D4"/></svg></div>
    <div><small>Call Us</small><b>(555)-014 2290</b></div>
  </div>
  <div class="btn btn-solid" style="left:949px;top:17px;width:110px;height:38px;font-size:13.5px">Contact us</div>
</header>
<nav class="abs nav">
  <a style="left:164px">Home</a>
  <a style="left:274px">Our Services</a>
  <a style="left:434px">About Us</a>
  <a style="left:568px">Technology</a>
  <a style="left:722px">Blog</a>
  <a style="left:824px">Testimonials</a>
  <a style="left:981px">Contact</a>
</nav>

<!-- Hero -->
<section class="abs hero" role="img" aria-label="Scientist in a lab coat writing on a clipboard with holographic data overlays">
</section>
<svg class="abs" style="left:0;top:540px" width="1200" height="180" viewBox="0 0 1200 180">
  <polygon points="0,12 600,128 1200,2 1200,180 0,180" fill="#0094D4"/>
  <polygon points="0,62 600,140 1200,50 1200,180 0,180" fill="#ffffff"/>
</svg>
<div class="abs hero-label">HEALTH TECHNOLOGY</div>
<h1 class="abs hero-title"><span class="l1">Revolutionizing</span><span class="l2">T-Cell Discovery</span></h1>
<p class="abs hero-text">VELQUO Delivers A Rapid, Versatile, Unbiased, And Cost-Effective Platform For Identifying Antigen-Specific T Cells, Powering The Next Generation Of Immunotherapy.</p>
<div class="btn btn-solid" style="left:144px;top:471px;width:144px;height:40px">Our Technology</div>
<div class="btn btn-outline" style="left:302px;top:471px;width:145px;height:40px">Download Brief</div>
<div class="abs scroll-cue"><svg width="22" height="22" viewBox="0 0 24 24" fill="none" stroke="#0094D4" stroke-width="2"><path d="M6 6l6 6 6-6M6 12l6 6 6-6"/></svg></div>

<!-- Platform -->
<div class="abs center" style="top:754px"><div class="eyebrow">The VELQUO Platform</div></div>
<h2 class="abs center section-title" style="top:780px">A cutting-edge solution for identifying</h2>
<div class="abs divider centered" style="left:0;width:1200px;top:832px"><span></span><span></span><span></span></div>

<div class="feature" style="left:141px">
  <svg width="48" height="40" viewBox="0 0 48 40" fill="none" stroke="#1f2a33" stroke-width="1.6"><circle cx="30" cy="20" r="11"/><circle cx="30" cy="20" r="5" stroke="#0094D4"/><path d="M2 14h12M6 20h10M2 26h12"/></svg>
  <h3>Rapid</h3>
  <p>Identify T cells in hours, not days, accelerating research and therapeutic development.</p>
</div>
<div class="feature active" style="left:376px">
  <svg width="48" height="40" viewBox="0 0 48 40" fill="none" stroke="#1f2a33" stroke-width="1.6"><path d="M8 30c6 0 10-4 16-4h10"/><path d="M6 34h10l10-2 12-6"/><circle cx="24" cy="12" r="6" stroke="#0094D4"/><path d="M24 2v4M24 18v4M14 12h4M30 12h4" stroke="#0094D4"/></svg>
  <h3>Versatile</h3>
  <p>Adaptable to multiple applications, from cancer therapy to autoimmune treatments.</p>
</div>
<div class="feature" style="left:611px">
  <svg width="48" height="40" viewBox="0 0 48 40" fill="none" stroke="#1f2a33" stroke-width="1.6"><circle cx="18" cy="14" r="11"/><path d="M18 6v16M12 10l6 4 6-4" stroke="#0094D4"/><path d="M6 36c4-6 20-6 24 0"/></svg>
  <h3>Unbiased</h3>
  <p>Ensures accurate detection without preconceived targeting biases.</p>
</div>
<div class="feature" style="left:847px">
  <svg width="48" height="40" viewBox="0 0 48 40" fill="none" stroke="#1f2a33" stroke-width="1.6"><path d="M4 32c6 0 10-4 16-4h10l8-4"/><rect x="16" y="12" width="5" height="10" stroke="#0094D4"/><rect x="24" y="7" width="5" height="15" stroke="#0094D4"/><path d="M14 8l8-5 8 4 6-4"/></svg>
  <h3>Cost-Effective</h3>
  <p>Cost-effective solution, making advanced immunotherapy accessible.</p>
</div>

<!-- About -->
<div class="abs" style="left:111px;top:1437px;width:66px;height:109px;background:var(--navy)"></div>
<div class="photo" role="img" aria-label="Researcher at a laptop with holographic healthcare icons" style="left:141px;top:1193px;width:404px;height:332px;background:linear-gradient(135deg,#e8eef2 0%,#9fb3bf 45%,#3d5566 100%)"></div>
<div class="abs" style="left:500px;top:1397px;width:86px;height:86px;border-radius:50%;background:var(--white);border:2px dashed var(--ink)"></div>
<div class="abs about-text" style="top:1184px"><div class="eyebrow">About Us</div></div>
<h2 class="abs section-title" style="left:599px;top:1208px">Global Research Partnerships</h2>
<div class="abs divider" style="left:601px;top:1259px"><span></span><span></span><span></span></div>
<p class="abs about-text body-copy" style="top:1278px">Lorem Ipsum is simply dummy text of the printing and typesetting industry. Lorem Ipsum has been the industry's standard dummy text ever since the 1500s, when an unknown printer took a galley of type and scrambled it to make a type specimen book. It has survived not only five centuries, but also the leap into electronic typesetting, remaining essentially unchanged</p>
<p class="abs about-text body-copy" style="top:1407px">Various versions have evolved over the years, sometimes by accident, sometimes on purpose (injected humour and the like). There are many variations of passages.</p>
<div class="btn btn-solid" style="left:599px;top:1489px;width:113px;height:38px;font-size:13px">Read More</div>
<div class="link" style="left:731px;top:1498px;font-size:13px">Call To Our Team</div>

<!-- Stats -->
<section class="abs stats">
  <div class="stat" style="left:93px"><b>40K</b><span>Happy Customer</span></div>
  <div class="stat-sep" style="left:346px"></div>
  <div class="stat" style="left:354px"><b>50+</b><span>Team Members</span></div>
  <div class="stat-sep" style="left:603px"></div>
  <div class="stat" style="left:623px"><b>14+</b><span>Year Of experience</span></div>
  <div class="stat-sep" style="left:884px"></div>
  <div class="stat" style="left:881px"><b>99%</b><span>Success Rate</span></div>
</section>
<svg class="abs" style="left:1100px;top:1606px" width="80" height="80" viewBox="0 0 80 80" fill="none" stroke="#fff" stroke-width="5"><path d="M40 4v72M4 40h72"/></svg>
<svg class="abs" style="left:51px;top:1863px" width="80" height="80" viewBox="0 0 80 80" fill="none" stroke="#fff" stroke-width="5"><path d="M40 4v72M4 40h72"/></svg>
<svg class="abs" style="left:580px;top:1902px" width="40" height="24" viewBox="0 0 40 24"><polygon points="0,0 40,0 20,22" fill="#00AB8E"/></svg>

<!-- Team -->
<div class="abs eyebrow" style="left:132px;top:2019px">About VELQUO</div>
<h2 class="abs section-title" style="left:130px;top:2043px">We are a team of innovators</h2>
<div class="abs divider" style="left:132px;top:2095px"><span></span><span></span><span></span></div>
<p class="abs body-copy" style="left:132px;top:2111px;width:420px">VELQUO is committed to revolutionizing T cell therapy by making identification faster, more precise, and accessible, empowering researchers and clinicians to develop life-saving treatments.</p>
<p class="abs body-copy" style="left:132px;top:2181px;width:440px">Our platform removes barriers in immunotherapy, enabling breakthroughs in cancer, autoimmune diseases, infectious diseases, and precision medicine.</p>
<div class="check" style="left:132px;top:2265px"><i><svg width="10" height="10" viewBox="0 0 12 12" fill="none" stroke="#fff" stroke-width="2"><path d="M2 6l3 3 5-6"/></svg></i>Founded by Leading Immunologists</div>
<div class="check" style="left:406px;top:2265px"><i><svg width="10" height="10" viewBox="0 0 12 12" fill="none" stroke="#fff" stroke-width="2"><path d="M2 6l3 3 5-6"/></svg></i>Patented Proprietary</div>
<div class="check" style="left:132px;top:2303px"><i><svg width="10" height="10" viewBox="0 0 12 12" fill="none" stroke="#fff" stroke-width="2"><path d="M2 6l3 3 5-6"/></svg></i>Global Research Partnerships</div>
<div class="abs" style="left:636px;top:2091px;width:16px;height:140px;background:var(--blue)"></div>
<div class="abs" style="left:1021px;top:2247px;width:67px;height:106px;background:var(--navy)"></div>
<div class="photo" role="img" aria-label="Group of smiling scientists in white lab coats" style="left:652px;top:2003px;width:404px;height:334px;border-radius:6px;background:linear-gradient(160deg,#d7dde2 0%,#f4f6f7 45%,#b9c4cc 100%)"></div>

<!-- Applications -->
<div class="abs center" style="top:2441px"><div class="eyebrow">Applications</div></div>
<h2 class="abs center section-title" style="top:2464px">Advancing immunotherapy across diverse diseases</h2>
<div class="abs divider centered" style="left:0;width:1200px;top:2517px"><span></span><span></span><span></span></div>

<div class="app" style="left:0;width:267px">
  <div class="photo" role="img" aria-label="Hands holding a red awareness ribbon" style="background:linear-gradient(135deg,#eef1f4,#c9d3da 60%,#c9343a 100%)"></div>
  <h3>Cancer Immunotherapy</h3>
  <p>Identify tumor-specific T cells for effective, low-side-effect therapies.</p>
</div>
<div class="app" style="left:302px;width:274px">
  <div class="photo" role="img" aria-label="Doctor examining a patient's neck" style="background:linear-gradient(135deg,#f2f4f6,#d7dde3 50%,#6f8aa0 100%)"></div>
  <h3>Autoimmune Disease</h3>
  <p>Target autoreactive T cells for precise autoimmune treatments.</p>
</div>
<div class="app" style="left:610px;width:274px">
  <div class="photo" role="img" aria-label="Gloved hands holding a petri dish in a lab" style="background:linear-gradient(135deg,#e6edf2,#aabfcd 55%,#2f7fc4 100%)"></div>
  <h3>Infectious Disease</h3>
  <p>Develop vaccines and treatments by identifying pathogen-specific T cells.</p>
</div>
<div class="app" style="left:919px;width:274px">
  <div class="photo" role="img" aria-label="Laboratory microscope examining a sample slide" style="background:linear-gradient(135deg,#5a6a78,#b9c6d0 55%,#e9eef1 100%)"></div>
  <h3>Precision Medicine</h3>
  <p>Enable tailored therapies by mapping patient-specific immune responses.</p>
</div>
<div class="btn btn-solid" style="left:506px;top:2892px;width:176px;height:42px;font-size:13.5px">Request a Demo</div>

<!-- Investment -->
<section class="abs invest" role="img" aria-label="Blue-tinted laboratory backdrop">
</section>
<div class="abs center" style="top:3079px"><div class="eyebrow" style="color:#fff">Investment Opportunity</div></div>
<h2 class="abs center section-title" style="top:3104px;color:#fff">Join us to shape the future of immunotherapy</h2>
<div class="abs divider centered" style="left:0;width:1200px;top:3156px"><span style="background:#fff"></span><span style="background:#C7EBF8"></span><span style="background:#fff"></span></div>

<div class="ibox" style="left:141px">
  <div class="ico"><svg width="30" height="30" viewBox="0 0 30 30" fill="#0094D4"><rect x="5" y="17" width="4" height="9"/><rect x="12" y="12" width="4" height="14"/><rect x="19" y="8" width="4" height="18"/><path d="M4 12l8-6 5 3 8-6" fill="none" stroke="#0094D4" stroke-width="2"/></svg></div>
  <h3>Market Potential</h3>
  <p>The cell therapy market is set to reach $20B by 2028, with T cell therapies driving growth.</p>
</div>
<div class="ibox" style="left:455px">
  <div class="ico strong"><svg width="30" height="30" viewBox="0 0 30 30" fill="none" stroke="#fff" stroke-width="2"><circle cx="15" cy="11" r="7"/><path d="M10 17l-2 10 7-3 7 3-2-10"/></svg></div>
  <h3>Competitive Edge</h3>
  <p>10x faster and 5x more cost-effective than existing methods, with broad applications.</p>
</div>
<div class="ibox" style="left:770px">
  <div class="ico"><svg width="30" height="30" viewBox="0 0 30 30" fill="none" stroke="#0094D4" stroke-width="2.4"><path d="M13 17l4-4"/><path d="M16 9l3-3a4 4 0 0 1 5 5l-3 3"/><path d="M14 21l-3 3a4 4 0 0 1-5-5l3-3"/></svg></div>
  <h3>IP Strength</h3>
  <p>Robust portfolio with multiple patents protecting our core technology.</p>
</div>
<div class="btn btn-line" style="left:392px;top:3468px;width:212px;height:42px">Connect with Our Team</div>
<div class="btn btn-line" style="left:620px;top:3468px;width:188px;height:42px">Download Pitch Deck</div>

<!-- Testimonials -->
<div class="abs center" style="top:3667px"><div class="eyebrow">Testimonials</div></div>
<h2 class="abs center section-title" style="top:3689px">What to say our client About us</h2>
<div class="abs divider centered" style="left:0;width:1200px;top:3743px"><span></span><span></span><span></span></div>
<div class="photo" role="img" aria-label="Professional woman working at a laptop in a bright office" style="left:137px;top:3790px;width:427px;height:279px;border-radius:0 0 24px 0;background:linear-gradient(135deg,#dfe6ea 0%,#b4c3cc 50%,#465866 100%)"></div>
<div class="abs quote-card">
  <div class="stars">
    <svg width="14" height="14" viewBox="0 0 24 24"><path d="M12 2l3 7 7 .6-5.4 4.7 1.7 7.2L12 17.8 5.7 21.5l1.7-7.2L2 9.6 9 9z" fill="#f7a21b"/></svg>
    <svg width="14" height="14" viewBox="0 0 24 24"><path d="M12 2l3 7 7 .6-5.4 4.7 1.7 7.2L12 17.8 5.7 21.5l1.7-7.2L2 9.6 9 9z" fill="#f7a21b"/></svg>
    <svg width="14" height="14" viewBox="0 0 24 24"><path d="M12 2l3 7 7 .6-5.4 4.7 1.7 7.2L12 17.8 5.7 21.5l1.7-7.2L2 9.6 9 9z" fill="#f7a21b"/></svg>
    <svg width="14" height="14" viewBox="0 0 24 24"><path d="M12 2l3 7 7 .6-5.4 4.7 1.7 7.2L12 17.8 5.7 21.5l1.7-7.2L2 9.6 9 9z" fill="#f7a21b"/></svg>
    <svg width="14" height="14" viewBox="0 0 24 24"><path d="M12 2l3 7 7 .6-5.4 4.7 1.7 7.2L12 17.8 5.7 21.5l1.7-7.2L2 9.6 9 9z" fill="#f7a21b"/></svg>
  </div>
  <p>Lorem Ipsum Is Simply Dummy Text Of The Printing And Typesetting Industry. Lorem Ipsum Has Been The Industry's Standard Dummy Text Ever Since The 1500s, When An Unknown Printer Took A Galley</p>
  <div class="person"><div class="avatar" role="img" aria-label="Client portrait"></div><div><b>Mara Delwin</b><span>Marketing Coordinator</span></div></div>
</div>
<div class="arrow-btn" style="top:3898px"><svg width="12" height="12" viewBox="0 0 24 24" fill="none" stroke="#1f2a33" stroke-width="2"><path d="M4 12h16M14 6l6 6-6 6"/></svg></div>
<div class="arrow-btn" style="top:3937px"><svg width="12" height="12" viewBox="0 0 24 24" fill="none" stroke="#1f2a33" stroke-width="2"><path d="M20 12H4M10 6l-6 6 6 6"/></svg></div>

<!-- Footer -->
<footer class="abs footer">
  <div class="abs brand" style="left:144px;top:73px"><i></i>VELQUOgen</div>
  <p class="abs" style="left:144px;top:130px;width:170px;font-size:12.5px;line-height:21px">Lorem Ipsum is simply dummy text of the printing and typesetting industry.</p>
  <div class="abs" style="left:144px;top:217px;display:flex;align-items:center;gap:8px;font-size:12.5px">Follow Us: <span class="social"></span><span class="social on"></span><span class="social"></span></div>

  <h4 style="left:429px">Quick Links</h4>
  <ul class="flist" style="left:429px"><li>Home</li><li>About Us</li><li>Technology</li><li>Blog</li><li>Contact</li></ul>

  <h4 style="left:610px">VELQUO Platform</h4>
  <ul class="flist" style="left:610px"><li>Rapid</li><li>Versatile</li><li>Unbiased</li><li>Cost-Effective</li></ul>

  <h4 style="left:822px">Contact Us</h4>
  <div class="fcontact" style="top:122px"><i><svg width="14" height="14" viewBox="0 0 24 24" fill="#fff"><path d="M12 2a7 7 0 0 0-7 7c0 5 7 13 7 13s7-8 7-13a7 7 0 0 0-7-7zm0 9.5A2.5 2.5 0 1 1 12 6.5a2.5 2.5 0 0 1 0 5z"/></svg></i><span>48 Meridian Way, Northfield Park,<br>MA 02199</span></div>
  <div class="fcontact" style="top:182px"><i class="blue"><svg width="14" height="14" viewBox="0 0 24 24" fill="#fff"><path d="M6.6 10.8a15 15 0 0 0 6.6 6.6l2.2-2.2a1 1 0 0 1 1-.25 11.4 11.4 0 0 0 3.6.57 1 1 0 0 1 1 1V20a1 1 0 0 1-1 1A17 17 0 0 1 3 4a1 1 0 0 1 1-1h3.5a1 1 0 0 1 1 1c0 1.25.2 2.45.57 3.57a1 1 0 0 1-.25 1z"/></svg></i><span>Phone: (617) 555-0188</span></div>
  <div class="fcontact" style="top:233px"><i><svg width="14" height="14" viewBox="0 0 24 24" fill="none" stroke="#fff" stroke-width="2"><rect x="3" y="5" width="18" height="14" rx="1"/><path d="M3 6l9 7 9-7"/></svg></i><span>info@velquogen.com</span></div>

  <div class="abs legal"><span>VELQUO is A Registered Trademark. Patents Pending</span><u>Privacy Policy &nbsp;|&nbsp; Terms Of Service</u></div>
</footer>

</div>
</body>
</html>
```